Bramble Hollow is company name.Handknit&crochet blankets&scarves. Need logo&business ...

I need a design that is eye catching, using yarn and is flowing. I'd like to see colors in aqua (Halvorsen Pike paint HP4817 Merilune) for the yarn and company name. For the text, a dark grey color (Halvorsen Pike HP5308 Velden Ash)

Colors
87cfc7

```html
<!DOCTYPE html>
<html lang="en">
<head>
<meta charset="utf-8">
<title>Bramble Hollow — Business Card</title>
<link href="https://fonts.googleapis.com/css2?family=Poppins:wght@400;500&family=Sacramento&display=swap" rel="stylesheet">
<style>
  :root {
    --aqua: #87cfc7;
    --ash: #5f5f5f;
    --paper: #ffffff;
    --backdrop: #1f1f21;
  }
  * { margin: 0; padding: 0; box-sizing: border-box; }
  html, body { width: 1200px; height: 1200px; overflow: hidden; }
  body {
    background: var(--backdrop);
    font-family: "Poppins", sans-serif;
    display: flex;
    flex-direction: column;
    align-items: center;
    justify-content: center;
    gap: 60px;
  }
  .card {
    width: 840px;
    height: 480px;
    position: relative;
    overflow: hidden;
    box-shadow: 0 14px 30px rgba(0,0,0,.45);
  }
  .card--front {
    background: var(--aqua);
    display: flex;
    align-items: center;
    justify-content: center;
  }
  .brand {
    display: flex;
    align-items: center;
    gap: 18px;
  }
  .brand__dot {
    width: 26px; height: 26px;
    border-radius: 50%;
  }
  .brand__name {
    font-family: "Poppins", sans-serif;
    font-weight: 400;
    font-size: 62px;
    letter-spacing: 1px;
    white-space: nowrap;
  }
  .card--front .brand__dot { background: var(--paper); }
  .card--front .brand__name { color: var(--paper); }

  .card--back { background: var(--paper); }
  .card--back .brand {
    position: absolute;
    top: 80px; left: 0; right: 0;
    justify-content: center;
  }
  .card--back .brand__dot { background: var(--aqua); }
  .card--back .brand__name { color: var(--aqua); }

  .contact-row {
    position: absolute;
    top: 250px; left: 50px; right: 40px;
    display: flex;
    align-items: center;
    gap: 26px;
  }
  .person {
    font-family: "Sacramento", cursive;
    font-size: 54px;
    line-height: 1.2;
    color: var(--ash);
    white-space: nowrap;
    flex: none;
  }
  .divider {
    width: 3px; height: 80px;
    background: var(--aqua);
    flex: none;
  }
  .details { list-style: none; flex: none; }
  .details li {
    display: flex;
    align-items: center;
    gap: 14px;
    font-size: 19px;
    color: var(--ash);
    line-height: 1.8;
    white-space: nowrap;
  }
  .details svg { width: 24px; height: 24px; flex: none; }

  .services {
    position: absolute;
    left: 0; right: 0;
    bottom: 40px;
    height: 46px;
    background: var(--aqua);
    color: var(--paper);
    font-size: 20px;
    font-weight: 500;
    display: flex;
    align-items: center;
    justify-content: center;
    white-space: nowrap;
    letter-spacing: .3px;
  }
</style>
</head>
<body>

  <section class="card card--front" aria-label="Card front">
    <div class="brand">
      <span class="brand__dot"></span>
      <span class="brand__name">Bramble Hollow</span>
    </div>
  </section>

  <section class="card card--back" aria-label="Card back">
    <div class="brand">
      <span class="brand__dot"></span>
      <span class="brand__name">Bramble Hollow</span>
    </div>

    <div class="contact-row">
      <p class="person">Rosalind Vaughn</p>
      <span class="divider"></span>
      <ul class="details">
        <li>
          <svg viewBox="0 0 24 24" aria-hidden="true"><circle cx="12" cy="12" r="12" fill="#87cfc7"/><path d="M9 6.5c.6 0 1.5 2 1.5 2.6 0 .6-.9 1-.9 1.5 0 .9 2.9 3.8 3.8 3.8.5 0 .9-.9 1.5-.9.6 0 2.6.9 2.6 1.5 0 1-1.2 2.5-2.6 2.5C11 17.5 6.5 13 6.5 9.1 6.5 7.7 8 6.5 9 6.5z" fill="#fff"/></svg>
          (555)284 619 3370
        </li>
        <li>
          <svg viewBox="0 0 24 24" aria-hidden="true"><circle cx="12" cy="12" r="12" fill="#87cfc7"/><rect x="6" y="8" width="12" height="8.5" rx="1" fill="none" stroke="#fff" stroke-width="1.4"/><path d="M6.5 8.5 12 13l5.5-4.5" fill="none" stroke="#fff" stroke-width="1.4"/></svg>
          hello@bramblehollowknits.com
        </li>
      </ul>
    </div>

    <p class="services">Handknit&amp;crochet | Baby&nbsp; Afghans | Afghans | scarves | Gloves | Hats</p>
  </section>

</body>
</html>
```